Kestrel Vale - Multifamily Development

Kestrel Vale is a Luxury Multifamily Development project located in Orange, NJ. This project will be completed in three phases with the first phase about 75% complete. Each phase will have a different name as follows
ALDER Kestrel Vale
WILLOW Kestrel Vale
JUNIPERS Kestrel Vale
We are going to install a banner on the side of the first building which will act as advertising for all buildings. We will eventually need advertising that will be in the windows as well as marketing materials . We want the marketing for this project to be similar for all three phases. At the moment, we are starting with this first simple banner. Attached is a rough idea of the look as well as our color palette. If you feel the color palette is a little too monochrome, feel free to propose an accent color. You can also visit our website to see more info on our company as well as the project. www.tarnvx.com Finally, if you need AI files (ie. for the logo), we can send to you. Thanks..

```html
<!DOCTYPE html>
<html lang="en">
<head>
<meta charset="utf-8">
<title>Kestrel Vale – Banner Series</title>
<link rel="stylesheet" href="https://fonts.googleapis.com/css2?family=Montserrat:wght@400;500;700;800&family=Cinzel:wght@400&display=swap">
<style>
  :root {
    --stage-light: #f4f4f4;
    --stage-dark: #c9c9c9;
    --brand-blue: #4a70a8;
    --navy: #1b2335;
    --slate: #3f4b66;
    --white: #ffffff;
    --sky: #b9cde3;
    --facade: #9a7c68;
  }
  * { box-sizing: border-box; margin: 0; padding: 0; }
  html, body { width: 1200px; height: 1100px; overflow: hidden; }
  body {
    background: radial-gradient(ellipse at 50% 45%, var(--stage-light) 0%, var(--stage-dark) 100%);
    font-family: "Montserrat", Arial, sans-serif;
    color: var(--white);
    position: relative;
  }
  .banner {
    position: absolute;
    top: 70px;
    width: 251px;
    height: 964px;
    display: flex;
    flex-direction: column;
    text-align: center;
  }
  .banner--alder { left: 134px; }
  .banner--willow { left: 474px; }
  .banner--junipers { left: 815px; }

  .rendering {
    flex: none;
    background: linear-gradient(180deg, var(--sky) 0%, #d8c8b4 40%, var(--facade) 75%, #6d6a66 100%);
  }
  .rendering--street { height: 161px; }
  .rendering--corner {
    height: 177px;
    background: linear-gradient(180deg, #cfdbe8 0%, #b89a8a 35%, #c7c2c0 70%, #8d8a88 100%);
  }

  .brand-band {
    flex: none;
    height: 139px;
    background: var(--brand-blue);
    display: flex;
    flex-direction: column;
    align-items: center;
    justify-content: center;
    gap: 14px;
    padding: 0 12px;
  }
  .brand-mark {
    flex: none;
    width: 16px;
    height: 16px;
    background: var(--white);
  }
  .brand-name {
    font-weight: 800;
    font-size: 20px;
    letter-spacing: 0.5px;
    text-transform: uppercase;
    line-height: 1;
    white-space: nowrap;
  }

  .title-band {
    flex: none;
    height: 165px;
    background: var(--navy);
    display: flex;
    flex-direction: column;
    justify-content: center;
    align-items: center;
    line-height: 0.98;
    white-space: nowrap;
  }
  .phase-name { font-weight: 800; letter-spacing: -0.5px; margin-bottom: 4px; }
  .banner--alder .phase-name { font-size: 58px; }
  .banner--willow .phase-name { font-size: 44px; }
  .banner--junipers .phase-name { font-size: 36px; }
  .project-name { font-weight: 500; font-size: 38px; letter-spacing: -0.5px; }

  .offer-band {
    flex: none;
    height: 262px;
    background: var(--navy);
    display: flex;
    flex-direction: column;
    align-items: center;
    padding-top: 22px;
  }
  .rule { width: 196px; height: 1px; background: var(--white); }
  .offer {
    font-family: "Cinzel", Georgia, serif;
    font-size: 30px;
    line-height: 1.17;
    letter-spacing: 1px;
    margin: 8px 0 10px;
    white-space: nowrap;
  }
  .call-label { font-size: 26px; font-weight: 400; margin-top: 22px; line-height: 1; }
  .phone { font-size: 31px; font-weight: 700; line-height: 1.2; letter-spacing: -0.3px; white-space: nowrap; }

  .email-band {
    flex: none;
    height: 30px;
    background: var(--slate);
    font-size: 15px;
    line-height: 30px;
  }
  .web-band {
    flex: none;
    height: 30px;
    background: var(--brand-blue);
    font-size: 18px;
    line-height: 30px;
  }
</style>
</head>
<body>

<section class="banner banner--alder">
  <div class="rendering rendering--street" role="img" aria-label="Architectural rendering of the mixed-facade apartment building at a street corner"></div>
  <div class="brand-band"><span class="brand-mark"></span><span class="brand-name">Tarn Properties</span></div>
  <div class="title-band">
    <div class="phase-name">ALDER</div>
    <div class="project-name">KESTREL<br>VALE</div>
  </div>
  <div class="rendering rendering--corner" role="img" aria-label="Rendering of the brick and stucco apartment building with pedestrians"></div>
  <div class="offer-band">
    <div class="rule"></div>
    <p class="offer">LUXURY<br>APARTMENT<br>RENTALS</p>
    <div class="rule"></div>
    <p class="call-label">CALL US</p>
    <p class="phone">555-014-2860</p>
  </div>
  <div class="email-band">Email: rentals@tarnvx.com</div>
  <div class="web-band">www.tarnvx.com</div>
</section>

<section class="banner banner--willow">
  <div class="rendering rendering--street" role="img" aria-label="Architectural rendering of the mixed-facade apartment building at a street corner"></div>
  <div class="brand-band"><span class="brand-mark"></span><span class="brand-name">Tarn Properties</span></div>
  <div class="title-band">
    <div class="phase-name">WILLOW</div>
    <div class="project-name">KESTREL<br>VALE</div>
  </div>
  <div class="rendering rendering--corner" role="img" aria-label="Rendering of the brick and stucco apartment building with pedestrians"></div>
  <div class="offer-band">
    <div class="rule"></div>
    <p class="offer">LUXURY<br>APARTMENT<br>RENTALS</p>
    <div class="rule"></div>
    <p class="call-label">CALL US</p>
    <p class="phone">555-014-2860</p>
  </div>
  <div class="email-band">Email: rentals@tarnvx.com</div>
  <div class="web-band">www.tarnvx.com</div>
</section>

<section class="banner banner--junipers">
  <div class="rendering rendering--street" role="img" aria-label="Architectural rendering of the mixed-facade apartment building at a street corner"></div>
  <div class="brand-band"><span class="brand-mark"></span><span class="brand-name">Tarn Properties</span></div>
  <div class="title-band">
    <div class="phase-name">JUNIPERS</div>
    <div class="project-name">KESTREL<br>VALE</div>
  </div>
  <div class="rendering rendering--corner" role="img" aria-label="Rendering of the brick and stucco apartment building with pedestrians"></div>
  <div class="offer-band">
    <div class="rule"></div>
    <p class="offer">LUXURY<br>APARTMENT<br>RENTALS</p>
    <div class="rule"></div>
    <p class="call-label">CALL US</p>
    <p class="phone">555-014-2860</p>
  </div>
  <div class="email-band">Email: rentals@tarnvx.com</div>
  <div class="web-band">www.tarnvx.com</div>
</section>

</body>
</html>
```